Qorvilo IT Website

We need a logo design for a new company in Jeffersonville, IN (serving predminately the Louisville, KY area). We merged Tarnwell Information Systems (an IT staffing company) and Cobalt Wayfarers (a business intelligence consulting group). Our logo was completed through Brush Market. We are doing a soft launch as we want one web page with just basic information and link that to the existing web pages we have: 1) www.tarnwellinfo.com and 2) www.cobaltwayfarers.com.
The 3 tabs we have in mind are:
Services/News/About Us. Under Services are: IT Staffing, Analytics/BI, Strategic Outsourcing, and CIO Services. Under About Us, we have History, Leadership and Contact Us. No submenu for News.
We also want to have the current companies' sites as clickable links. One should be IT Staffing (directed to www.tarnwellinfo.com) and the other should be Business Intelligence/Data Analytics (directed to www.cobaltwayfarers.com).
Target Market(s)
IT professionals and clients needing IT services
Industry/Entity Type
It Company
Coding
Coded - Design and coding required
Number of Pages Required
4 page
Look and feel

```html
<!DOCTYPE html>
<html lang="en">
<head>
<meta charset="utf-8">
<title>Qorvilo IT</title>
<link href="https://fonts.googleapis.com/css2?family=Open+Sans:wght@400;600;700&family=Roboto+Condensed:wght@400;700&display=swap" rel="stylesheet">
<style>
:root{
  --blue:#1f8ad9;
  --blue-dark:#1669b0;
  --navy:#163a6a;
  --ink:#222a33;
  --muted:#5d6670;
  --line:#d6dbe0;
  --paper:#ffffff;
  --mist:#f1f3f5;
  --dusk:#2b2f35;
}
*{box-sizing:border-box;margin:0;padding:0}
html,body{width:1200px;height:3760px;overflow:hidden;background:var(--paper)}
body{font-family:"Open Sans",Arial,sans-serif;color:var(--ink);font-size:14px;line-height:1.55}
.page{position:relative;width:1200px;height:3760px}
.section{position:relative;width:1200px;overflow:hidden}
.heading{font-family:"Roboto Condensed","Arial Narrow",sans-serif;font-weight:700;text-transform:uppercase;font-size:34px;text-align:center;letter-spacing:.5px}
.heading-rule{display:block;width:120px;height:3px;margin:10px auto 0;background:currentColor}

/* header */
.site-header{height:112px;background:var(--paper)}
.brand{position:absolute;left:56px;top:18px;display:flex;align-items:center;gap:10px}
.brand-mark{width:34px;height:34px;background:var(--blue)}
.brand-name{font-family:"Open Sans",sans-serif;font-weight:700;font-size:34px;color:var(--navy);letter-spacing:.5px}
.contact-bar{position:absolute;right:48px;top:22px;display:flex;gap:34px;font-weight:600;font-size:17px;color:var(--navy)}
.contact-bar span{display:flex;align-items:center;gap:8px}
.contact-bar svg{width:22px;height:22px}
.main-nav{position:absolute;left:250px;top:64px;height:42px;width:920px;background:var(--blue);display:flex}
.main-nav a{color:#fff;text-decoration:none;font-size:13px;font-weight:600;padding:0 18px;line-height:42px}
.main-nav a.is-current{background:var(--blue-dark)}

/* hero */
.hero{height:608px}
.hero-photo{position:absolute;inset:0;background:linear-gradient(90deg,#f4f5f6 0%,#e9eaeb 35%,#b8b2aa 62%,#6f6157 80%,#3f3a38 100%)}
.hero-copy{position:absolute;left:60px;top:240px;width:400px}
.hero-title{font-family:"Roboto Condensed",sans-serif;font-weight:700;font-size:34px;color:var(--navy);margin-bottom:14px}
.hero-copy p{font-size:13px;color:var(--ink)}
.btn{display:inline-block;background:var(--blue);color:#fff;font-size:14px;font-weight:600;padding:8px 26px;text-decoration:none}
.hero-copy .btn{margin-top:20px}
.hero-dots{position:absolute;left:60px;bottom:30px;display:flex;gap:10px}
.hero-dots i{width:12px;height:12px;border-radius:50%;background:#c6ccd2;display:block}
.hero-dots i:first-child{background:var(--blue)}

/* about */
.about{height:540px;background:var(--blue);color:#fff}
.about .heading{padding-top:46px}
.about-intro{width:900px;margin:26px auto 0;text-align:center;font-size:13px}
.about-cards{position:absolute;left:100px;top:300px;width:1000px;display:flex;justify-content:space-between}
.about-card{width:300px;height:200px;text-align:center;padding:24px 22px}
.about-card.is-featured{background:var(--blue-dark)}
.about-card svg{width:56px;height:56px}
.about-card h3{font-family:"Roboto Condensed",sans-serif;font-size:21px;margin:10px 0 6px}
.about-card p{font-size:12px}

/* services */
.services{height:500px;background:var(--paper)}
.services .heading{color:var(--navy);padding-top:40px}
.services-photo{position:absolute;left:70px;top:150px;width:300px;height:300px;border-radius:50%;background:radial-gradient(circle at 45% 40%,#f2f5f8,#bcd0e2 60%,#6b87a6)}
.services-copy{position:absolute;left:420px;top:200px;width:720px}
.services-copy h3{font-family:"Roboto Condensed",sans-serif;font-size:30px;color:var(--ink);margin-bottom:14px}
.services-copy p{font-size:13px;color:var(--muted)}
.services-copy .btn{margin-top:24px}
.pager{position:absolute;right:38px;top:430px;display:flex;gap:4px}
.pager span{width:28px;height:26px;border:1px solid var(--line);display:flex;align-items:center;justify-content:center}

/* team */
.team{height:600px;background:var(--mist)}
.team .heading{padding-top:40px;color:var(--ink)}
.team-list{position:absolute;left:110px;top:170px;width:980px;display:flex;justify-content:space-between}
.member{width:300px;text-align:center}
.member-photo{width:300px;height:300px;border-radius:50%;border:5px solid var(--navy);padding:6px;background:var(--paper)}
.member-photo div{width:100%;height:100%;border-radius:50%}
.member h3{font-family:"Roboto Condensed",sans-serif;font-size:25px;margin-top:10px}
.member .role{display:inline-block;background:var(--navy);color:#fff;font-size:12px;padding:2px 14px}
.member-social{position:absolute;left:92px;top:256px;display:flex;gap:8px;background:var(--blue);padding:6px 14px;border-radius:12px}
.member-social i{width:14px;height:14px;border-radius:50%;background:#fff;display:block}
.team-arrow{position:absolute;top:310px}
.team-arrow svg{width:30px;height:46px}

/* testimonials */
.testimonials{height:360px;color:#fff}
.testimonials-bg{position:absolute;inset:0;background:linear-gradient(180deg,#3b3f45,#22262b)}
.testimonials .heading{position:relative;padding-top:40px;color:#fff}
.quote{position:relative;width:900px;margin:34px auto 0;text-align:center;font-size:13px;color:#e3e6ea}
.quote cite{display:block;margin-top:14px;font-style:italic;color:#aeb5bd}

/* news & blog */
.updates{height:430px;display:flex;gap:60px;padding:40px 60px 0}
.updates-col{flex:1}
.updates-col h2{font-family:"Roboto Condensed",sans-serif;font-size:28px;color:var(--blue);text-transform:uppercase;border-bottom:2px solid var(--line);padding-bottom:6px;margin-bottom:18px}
.post{display:flex;gap:16px;margin-bottom:26px}
.post-thumb{flex:0 0 150px;height:100px;background:linear-gradient(135deg,#8ea9c3,#3f5a78)}
.post h3{font-size:14px;font-weight:700;color:var(--navy)}
.post p{font-size:12px;color:var(--muted)}
.post time{display:block;font-size:11px;color:var(--blue);margin-top:4px}

/* footer */
.footer-brand{height:130px;border-top:1px solid var(--line);text-align:center;padding-top:22px}
.footer-brand .brand{position:static;justify-content:center}
.footer-brand .brand-name{font-size:30px}
.footer-brand address{font-style:normal;font-size:12px;color:var(--muted);margin-top:6px}
.social{display:flex;justify-content:center;gap:8px;margin-top:8px}
.social i{width:22px;height:22px;border-radius:50%;background:#8c949c;display:block}
.footer-links{height:400px;display:flex;padding:50px 60px 0;border-top:1px solid var(--line)}
.footer-links div{flex:1}
.footer-links h4{font-size:18px;font-weight:700;margin-bottom:14px}
.footer-links a{display:block;font-size:14px;color:var(--ink);text-decoration:none;line-height:2}
.copyright{position:absolute;left:0;top:3690px;width:1200px;height:70px;border-top:1px solid var(--line);padding:24px 60px;font-size:12px;color:var(--muted)}
</style>
</head>
<body>
<div class="page">

<header class="section site-header">
  <div class="brand"><span class="brand-mark"></span><span class="brand-name">Qorvilo IT</span></div>
  <div class="contact-bar">
    <span><svg viewBox="0 0 24 24"><circle cx="12" cy="12" r="12" fill="#1f8ad9"/><path d="M8 6l2 0 1 3-1.5 1a7 7 0 0 0 3.5 3.5l1-1.5 3 1v2c0 1-1 2-2 2A10 10 0 0 1 6 8c0-1 1-2 2-2z" fill="#fff"/></svg>(555) 014-2290</span>
    <span><svg viewBox="0 0 24 24"><circle cx="12" cy="12" r="12" fill="#1f8ad9"/><rect x="6" y="8" width="12" height="8" fill="#fff"/><path d="M6 8l6 5 6-5" stroke="#1f8ad9" stroke-width="1.4" fill="none"/></svg>hello@qorviloit.com</span>
  </div>
  <nav class="main-nav">
    <a class="is-current" href="#">HOME</a><a href="#">Services</a><a href="#">Our Team</a><a href="#">Testimonials</a><a href="#">Contact us</a><a href="#">Resources</a><a href="#">Careers</a><a href="#">Employee Benefits</a>
  </nav>
</header>

<section class="section hero">
  <div class="hero-photo" role="img" aria-label="Photo of two businessmen smiling at a laptop in an office"></div>
  <div class="hero-copy">
    <h1 class="hero-title">We Can Bring Your Data To Life.</h1>
    <p>Our team turns scattered records into clear reports, steady systems and sharp decisions. We pair skilled people with proven analytics so every project moves faster and lands with confidence.</p>
    <a class="btn" href="#">Read More</a>
  </div>
  <div class="hero-dots"><i></i><i></i></div>
</section>

<section class="section about">
  <h2 class="heading">About Us<span class="heading-rule"></span></h2>
  <p class="about-intro">Qorvilo IT brings together staffing expertise and business intelligence under one roof. For years our founders have placed trusted technical talent across the region and helped companies read their data with clarity. Today we combine both strengths to serve clients who need dependable people, smart insight and a partner that stays the course.</p>
  <div class="about-cards">
    <div class="about-card">
      <svg viewBox="0 0 56 56"><circle cx="28" cy="28" r="27" fill="#163a6a"/><circle cx="28" cy="22" r="8" fill="#fff"/><path d="M14 42c2-8 8-11 14-11s12 3 14 11z" fill="#fff"/></svg>
      <h3>Our Experience</h3>
      <p>Decades of placing IT talent and guiding data projects for firms of every size.</p>
    </div>
    <div class="about-card is-featured">
      <svg viewBox="0 0 56 56"><circle cx="28" cy="28" r="27" fill="#163a6a"/><rect x="16" y="30" width="6" height="12" fill="#fff"/><rect x="25" y="22" width="6" height="20" fill="#fff"/><rect x="34" y="14" width="6" height="28" fill="#fff"/></svg>
      <h3>Our Skills</h3>
      <p>Staffing, analytics, BI, outsourcing and CIO advisory delivered by one focused team.</p>
    </div>
    <div class="about-card">
      <svg viewBox="0 0 56 56"><circle cx="28" cy="28" r="27" fill="#163a6a"/><path d="M17 29l8 8 15-17" stroke="#fff" stroke-width="4" fill="none"/></svg>
      <h3>What We Done ?</h3>
      <p>Hundreds of placements and dashboards that keep local businesses running strong.</p>
    </div>
  </div>
</section>

<section class="section services">
  <h2 class="heading">Our Services<span class="heading-rule"></span></h2>
  <div class="services-photo" role="img" aria-label="Photo of business people in silhouette beside a city skyline"></div>
  <div class="services-copy">
    <h3>Information Systems</h3>
    <p>We design, support and secure the systems your business relies on every day. From network planning to software rollouts, our specialists keep your technology aligned with your goals, so your staff can focus on the work that matters most and your data stays safe, organized and ready when you need it.</p>
    <a class="btn" href="#">Read More</a>
  </div>
  <div class="pager">
    <span><svg width="10" height="14" viewBox="0 0 10 14"><path d="M8 1L2 7l6 6" stroke="#5d6670" stroke-width="2" fill="none"/></svg></span>
    <span><svg width="10" height="14" viewBox="0 0 10 14"><path d="M2 1l6 6-6 6" stroke="#5d6670" stroke-width="2" fill="none"/></svg></span>
  </div>
</section>

<section class="section team">
  <h2 class="heading">Our Team<span class="heading-rule"></span></h2>
  <span class="team-arrow" style="left:40px"><svg viewBox="0 0 30 46"><path d="M24 3L6 23l18 20" stroke="#1f8ad9" stroke-width="5" fill="none"/></svg></span>
  <span class="team-arrow" style="right:40px"><svg viewBox="0 0 30 46"><path d="M6 3l18 20L6 43" stroke="#1f8ad9" stroke-width="5" fill="none"/></svg></span>
  <div class="team-list">
    <div class="member" style="position:relative">
      <div class="member-photo"><div role="img" aria-label="Portrait photo of team member" style="background:linear-gradient(160deg,#b9c8d6,#6e7f90)"></div></div>
      <div class="member-social"><i></i><i></i><i></i></div>
      <h3>Lena Harwick</h3><span class="role">Co Founder</span>
    </div>
    <div class="member">
      <div class="member-photo"><div role="img" aria-label="Portrait photo of team member" style="background:linear-gradient(160deg,#6c6f73,#2d3034)"></div></div>
      <h3>Owen Pell</h3><span class="role">Web Developer</span>
    </div>
    <div class="member">
      <div class="member-photo"><div role="img" aria-label="Portrait photo of team member" style="background:linear-gradient(160deg,#d7dbe0,#8a9098)"></div></div>
      <h3>Miles Tovar</h3><span class="role">Graphic Designer</span>
    </div>
  </div>
</section>

<section class="section testimonials">
  <div class="testimonials-bg" role="img" aria-label="Dim photo of a crowd of professionals"></div>
  <h2 class="heading">Testimonials<span class="heading-rule"></span></h2>
  <blockquote class="quote">Working with this team changed how we hire and how we plan. They found the right engineers in weeks, then built reports that finally showed us where our time and budget were going. Clear, honest and always on call, they feel like part of our own staff.<cite>Dana Whitcomb, Operations Lead</cite></blockquote>
</section>

<section class="section updates">
  <div class="updates-col">
    <h2>News</h2>
    <article class="post"><div><h3>New analytics practice opens in Louisville</h3><p>We now offer full BI consulting to clients across the river region, from dashboards to data strategy.</p><time>Apr 12</time></div></article>
    <article class="post"><div><h3>Staffing team grows with six new recruiters</h3><p>Our recruiting group expands to meet rising demand for developers, analysts and project managers.</p><time>Mar 28</time></div></article>
  </div>
  <div class="updates-col">
    <h2>Blog</h2>
    <article class="post"><div class="post-thumb" role="img" aria-label="Photo of a hand using a tablet"></div><div><h3>Five signs your reports need a refresh</h3><p>Stale numbers slow every decision. Here is how to spot gaps before they cost you.</p></div></article>
    <article class="post"><div class="post-thumb" role="img" aria-label="Photo of a laptop keyboard"></div><div><h3>Hiring contract talent the smart way</h3><p>A short guide to scoping roles, setting rates and onboarding contractors without delays.</p></div></article>
  </div>
</section>

<section class="section footer-brand">
  <div class="brand"><span class="brand-mark"></span><span class="brand-name">Qorvilo IT</span></div>
  <address>214 Riverside Parkway, Suite 300, Jeffersonville, IN 47130 | (555) 014-2290 | hello@qorviloit.com</address>
  <div class="social"><i></i><i></i><i></i><i></i><i></i><i></i></div>
</section>

<footer class="section footer-links">
  <div><h4>News &amp; Media</h4><a href="#">Latest Stories</a><a href="#">Press Releases</a><a href="#">Media Inquiries</a><a href="#">Media Partners</a><a href="#">The News</a></div>
  <div><h4>Support</h4><a href="#">Latest Stories</a><a href="#">Press Releases</a><a href="#">Media Inquiries</a><a href="#">Media Partners</a><a href="#">The News</a></div>
  <div><h4>Event</h4><a href="#">Latest Stories</a><a href="#">Press Releases</a><a href="#">Media Inquiries</a><a href="#">Media Partners</a><a href="#">The News</a></div>
  <div><h4>News &amp; Media</h4><a href="#">Submit Your Story</a><a href="#">Member Updates Archive</a><a href="#">Contact</a><a href="#">Login</a></div>
</footer>

<div class="copyright">© QorviloIT.com , 2016, All Rights reserved. &nbsp; Privacy Policy | Legal Usage Policy | Sitemap</div>

</div>
</body>
</html>
```